Layout for new page on existing website

We have an existing website (www.brightloomworks.org) and need a new page designing to promote a new product.
The new page needs to be consistent with the existing website look and feel (www.brightloomworks.org) but current persistent elements on the standard page design can be moved/removed from the page to accommodate a new layout necessary for getting all the content laid out in a logical user friendly way.
The content required for the page is attached along with a wireframe mock up that may help understand the expectation, however the wireframe was just created to help me work out what was needed on the page and the layout can be different. A key element is the quality of the design of each of the artifacts (e.g. the panel the embedded video needs to go in, icons etc) and a clear display of the information.
Updates
The website that the new page needs to fit into is www.brightloomworks.org, i will also added the company logo to the brief.
Our Corporate Colours
- Green: #A2FF00
- Cream: #FFFF99
- Yellow: #FFE900
- Grey: #534741
Industry/Entity Type
Product
Look and feel
Each slider illustrates characteristics of the customer's brand and the style your logo design should communicate.

```html
<!DOCTYPE html>
<html lang="en">
<head>
<meta charset="utf-8">
<title>Brightloom Works – Course Management and Booking</title>
<link rel="stylesheet" href="https://fonts.googleapis.com/css2?family=Open+Sans:wght@400;600;700&display=swap">
<style>
:root{
  --grey:#534741;
  --grey-dark:#463b36;
  --grey-deep:#3a302b;
  --green:#A2FF00;
  --green-soft:#9bd11f;
  --cream:#FFFF99;
  --yellow:#FFE900;
  --white:#ffffff;
  --field:#675b55;
  --field-edge:#3e3430;
  --muted:#8e837c;
  --ink:#2b3320;
}
*{box-sizing:border-box;margin:0;padding:0}
html,body{width:1200px;height:2984px;overflow:hidden}
body{background:var(--grey);font-family:"Open Sans",Arial,sans-serif;color:var(--white);position:relative}
.page{position:absolute;left:0;top:0;width:1200px;height:2984px;
  background:linear-gradient(90deg,var(--grey-dark) 0,var(--grey) 180px,var(--grey) 1020px,var(--grey-dark) 1200px)}
.abs{position:absolute}

.home-link{left:162px;top:78px;width:56px;text-align:center;font-size:14px;font-weight:600;color:var(--white);text-decoration:none}
.home-link svg{display:block;margin:0 auto 10px}

.brand{left:0;width:1200px;top:100px;text-align:center;font-weight:700;font-size:34px;letter-spacing:8px;color:var(--white)}
.brand .dot{display:inline-block;width:22px;height:22px;border-radius:50%;background:var(--green);margin-left:14px;vertical-align:middle}

.tagline{left:0;width:1220px;top:190px;text-align:center;font-size:26px;color:var(--cream)}

.banner{left:222px;top:250px;width:776px;height:232px;border-radius:14px;overflow:hidden;
  background:linear-gradient(180deg,#e5ffb0 0,#c8f55a 40%,var(--green-soft) 41%,#8fcf12 100%);
  box-shadow:0 22px 30px -14px rgba(0,0,0,.5)}
.banner-title{position:absolute;left:34px;top:104px;width:300px;font-size:36px;line-height:46px;font-weight:600;color:var(--ink)}
.banner-screens{position:absolute;left:352px;top:14px;width:416px;height:212px;transform:skewY(-6deg);
  background:linear-gradient(135deg,#1f3a8a,#3d6fd0 45%,#cfe3f7 70%,#3aa8e0)}

.video{left:222px;top:572px;width:388px;height:346px;background:#000;box-shadow:0 14px 20px -10px rgba(0,0,0,.6)}
.video-bar{position:absolute;left:0;bottom:0;width:100%;height:22px;background:linear-gradient(#f2f2f2,#c9c9c9)}
.video-spinner{position:absolute;left:194px;top:152px}

.quote-mark{font-family:Georgia,serif;font-size:180px;line-height:1;color:var(--grey-deep);font-weight:700}
.quote-open{left:642px;top:540px}
.quote-close{left:910px;top:800px}
.quote-text{left:672px;top:612px;width:300px;font-size:20px;line-height:26px}
.quote-cite{left:672px;top:812px;width:302px;text-align:right;font-size:13px;line-height:18px}
.quote-cite a{color:var(--green);text-decoration:none}

.section-title{font-size:28px;color:var(--cream);font-weight:400}

.feature{width:370px;font-size:16px;line-height:21px}
.feature-icon{float:left;width:100px;height:84px;margin:0 12px 4px 0}
.feature h3{font-size:16px;font-weight:600;color:var(--green);line-height:21px}

.benefits{left:222px;top:1846px;width:760px;list-style:none}
.benefits li{position:relative;padding-left:34px;font-size:16px;line-height:21px;margin-bottom:13px}
.benefits li svg{position:absolute;left:0;top:1px}

.contact-title{left:222px;top:2418px;width:760px;font-size:28px;line-height:36px;font-weight:400;color:var(--cream)}
.contact-form{left:222px;top:2522px;width:760px}
.field{display:flex;align-items:center;height:40px;margin-bottom:13px}
.field label{width:122px;font-size:18px}
.field span{display:block;width:620px;height:40px;background:var(--field);border:2px solid var(--field-edge)}
.submit{display:block;margin:14px 0 0 122px;width:176px;height:58px;border:0;border-radius:12px;
  background:linear-gradient(#d6ff80,var(--green) 50%,#7cc400);font-family:inherit;font-size:26px;font-weight:700;color:var(--ink)}

.footer{left:0;width:1320px;top:2872px;text-align:center;font-size:12px;color:var(--muted)}
</style>
</head>
<body>
<div class="page">

  <a class="abs home-link" href="#">
    <svg width="50" height="44" viewBox="0 0 50 44" aria-hidden="true">
      <path d="M4 22 L25 4 L46 22" fill="none" stroke="#FFE900" stroke-width="4" stroke-linejoin="round"/>
      <rect x="11" y="20" width="28" height="21" fill="none" stroke="#FFE900" stroke-width="4"/>
      <rect x="20" y="27" width="10" height="14" fill="#FFE900"/>
    </svg>
    Home
  </a>

  <div class="abs brand">BRIGHTLOOM WORKS<span class="dot"></span></div>

  <p class="abs tagline">Course Management and Booking Simplified</p>

  <div class="abs banner">
    <h1 class="banner-title">Built with your<br>business in mind</h1>
    <div class="banner-screens" role="img" aria-label="Collage of client booking website screenshots"></div>
  </div>

  <div class="abs video" role="img" aria-label="Embedded product video player">
    <svg class="video-spinner" width="22" height="22" viewBox="0 0 22 22" aria-hidden="true">
      <g stroke="#bbb" stroke-width="2.5" stroke-linecap="round">
        <line x1="11" y1="2" x2="11" y2="6"/><line x1="11" y1="16" x2="11" y2="20" opacity=".4"/>
        <line x1="2" y1="11" x2="6" y2="11" opacity=".6"/><line x1="16" y1="11" x2="20" y2="11" opacity=".8"/>
        <line x1="4.6" y1="4.6" x2="7.4" y2="7.4" opacity=".5"/><line x1="14.6" y1="14.6" x2="17.4" y2="17.4" opacity=".9"/>
      </g>
    </svg>
    <div class="video-bar"></div>
  </div>

  <div class="abs quote-mark quote-open" aria-hidden="true">&ldquo;</div>
  <div class="abs quote-mark quote-close" aria-hidden="true">&rdquo;</div>
  <blockquote class="abs quote-text">&ldquo;A convenient tool that was simple to integrate into our website. It has allowed both the business and our customers an easy way to book courses. In life sometimes simple is good and this is a great example!&rdquo;</blockquote>
  <p class="abs quote-cite">Helen Marsh, Director @ Trailmark Coaching<br><a href="#">www.trailmarkcoach.org</a></p>

  <h2 class="abs section-title" style="left:222px;top:988px">Key Features:</h2>

  <div class="abs feature" style="left:222px;top:1052px">
    <svg class="feature-icon" viewBox="0 0 90 80" aria-hidden="true">
      <ellipse cx="40" cy="74" rx="34" ry="4" fill="#2f2622"/>
      <circle cx="40" cy="36" r="28" fill="none" stroke="#FFE900" stroke-width="4"/>
      <path d="M40 18 V38 H54" fill="none" stroke="#FFE900" stroke-width="4" stroke-linecap="round"/>
    </svg>
    <h3>Available and easy to use 24/7</h3>By allowing booking and payment at any time of the day, your attendees will be more likely to commit to your event and with no account setup or password required and no paper forms to fill in and post, booking onto and paying for your courses is easy.
  </div>

  <div class="abs feature" style="left:640px;top:1052px">
    <svg class="feature-icon" viewBox="0 0 90 80" aria-hidden="true">
      <ellipse cx="40" cy="74" rx="34" ry="4" fill="#2f2622"/>
      <g fill="none" stroke="#FFE900" stroke-width="4">
        <rect x="14" y="6" width="16" height="26" rx="8" transform="rotate(-35 22 19)"/>
        <rect x="28" y="24" width="16" height="26" rx="8" transform="rotate(-35 36 37)"/>
        <rect x="42" y="42" width="16" height="26" rx="8" transform="rotate(-35 50 55)"/>
      </g>
    </svg>
    <h3>Online Course promotion</h3>List your upcoming courses in a clear and simple way so people can easily find and select the course that suits them.
  </div>

  <div class="abs feature" style="left:222px;top:1278px">
    <svg class="feature-icon" viewBox="0 0 90 80" aria-hidden="true">
      <ellipse cx="40" cy="74" rx="34" ry="4" fill="#2f2622"/>
      <path d="M40 8 L68 60 H12 Z" fill="none" stroke="#FFE900" stroke-width="4" stroke-linejoin="round"/>
      <path d="M22 30 l6 -2 l-1 7 M58 30 l-6 -2 l1 7 M40 66 l-5 -5 M40 66 l-5 5" fill="none" stroke="#FFE900" stroke-width="3"/>
    </svg>
    <h3>Online &amp; Offline Payments</h3>Take payments online, whilst having the flexibility of managing and adding offline payments.
  </div>

  <div class="abs feature" style="left:640px;top:1278px">
    <svg class="feature-icon" viewBox="0 0 90 80" aria-hidden="true">
      <ellipse cx="40" cy="74" rx="34" ry="4" fill="#2f2622"/>
      <g fill="none" stroke="#FFE900" stroke-width="4" stroke-linejoin="round">
        <path d="M8 28 L66 8 L58 64 Z"/>
        <path d="M8 28 L44 40 L66 8 M44 40 L58 64"/>
      </g>
    </svg>
    <h3>Built in email system</h3>Enable quick and easy communication with upcoming course candidates and promotion of additional courses to past candidates.
  </div>

  <div class="abs feature" style="left:222px;top:1432px">
    <svg class="feature-icon" viewBox="0 0 90 80" aria-hidden="true">
      <ellipse cx="40" cy="74" rx="34" ry="4" fill="#2f2622"/>
      <g fill="none" stroke="#FFE900" stroke-width="4" stroke-linejoin="round">
        <path d="M46 6 L58 14 L28 60 L16 66 L16 52 Z"/>
        <path d="M16 66 L42 68"/>
      </g>
    </svg>
    <h3>Customisable look and feel</h3>All elements of the booking systems design will fit in with your existing websites style.
  </div>

  <div class="abs feature" style="left:640px;top:1434px">
    <svg class="feature-icon" viewBox="0 0 90 80" aria-hidden="true">
      <ellipse cx="40" cy="74" rx="34" ry="4" fill="#2f2622"/>
      <g fill="none" stroke="#FFE900" stroke-width="4">
        <ellipse cx="50" cy="28" rx="16" ry="22" transform="rotate(40 50 28)"/>
        <path d="M40 20 L56 36"/>
        <path d="M34 46 C20 56 28 66 12 64"/>
      </g>
    </svg>
    <h3>Live course place availability</h3>By defining minimum and maximum candidates permitted on a course its easy to prevent overbooking and also prevent courses running that don&rsquo;t have enough candidates.
  </div>

  <div class="abs feature" style="left:222px;top:1634px">
    <svg class="feature-icon" viewBox="0 0 90 80" aria-hidden="true">
      <ellipse cx="40" cy="74" rx="34" ry="4" fill="#2f2622"/>
      <g fill="none" stroke="#FFE900" stroke-width="4" stroke-linejoin="round">
        <path d="M14 18 L46 6 L64 52 L32 64 Z"/>
        <path d="M24 24 L46 16 M28 34 L50 26 M32 44 L54 36"/>
      </g>
    </svg>
    <h3>Venue database management</h3>Easily add, edit and remove venues from which you operate your courses from.
  </div>

  <h2 class="abs section-title" style="left:222px;top:1782px">Key Benefits:</h2>

  <ul class="abs benefits">
    <li><svg width="22" height="18" viewBox="0 0 22 18" aria-hidden="true"><path d="M2 9 L8 15 L20 3" fill="none" stroke="#A2FF00" stroke-width="5" stroke-linejoin="round"/></svg>Live Availability – Availability on course place availability to prevent &nbsp;overbooking</li>
    <li><svg width="22" height="18" viewBox="0 0 22 18" aria-hidden="true"><path d="M2 9 L8 15 L20 3" fill="none" stroke="#A2FF00" stroke-width="5" stroke-linejoin="round"/></svg>Customers can search for Courses and Book Online with immediate confirmation</li>
    <li><svg width="22" height="18" viewBox="0 0 22 18" aria-hidden="true"><path d="M2 9 L8 15 L20 3" fill="none" stroke="#A2FF00" stroke-width="5" stroke-linejoin="round"/></svg>Automated confirmation emails</li>
    <li><svg width="22" height="18" viewBox="0 0 22 18" aria-hidden="true"><path d="M2 9 L8 15 L20 3" fill="none" stroke="#A2FF00" stroke-width="5" stroke-linejoin="round"/></svg>Be available for business 24/7 and take orders anytime! Customers can book when it&rsquo;s most convenient for them – be it early morning, late evening or weekend</li>
    <li><svg width="22" height="18" viewBox="0 0 22 18" aria-hidden="true"><path d="M2 9 L8 15 L20 3" fill="none" stroke="#A2FF00" stroke-width="5" stroke-linejoin="round"/></svg>No fielding phone calls, no wading through paper registrations. Attendees book on your website, there and then</li>
    <li><svg width="22" height="18" viewBox="0 0 22 18" aria-hidden="true"><path d="M2 9 L8 15 L20 3" fill="none" stroke="#A2FF00" stroke-width="5" stroke-linejoin="round"/></svg>No more trips to the bank, take immediate and secure payments online</li>
    <li><svg width="22" height="18" viewBox="0 0 22 18" aria-hidden="true"><path d="M2 9 L8 15 L20 3" fill="none" stroke="#A2FF00" stroke-width="5" stroke-linejoin="round"/></svg>Automated confirmation emails so reducing the time need communicating with candidates</li>
    <li><svg width="22" height="18" viewBox="0 0 22 18" aria-hidden="true"><path d="M2 9 L8 15 L20 3" fill="none" stroke="#A2FF00" stroke-width="5" stroke-linejoin="round"/></svg>Boost course bookings and reduce administrative time and costs</li>
    <li><svg width="22" height="18" viewBox="0 0 22 18" aria-hidden="true"><path d="M2 9 L8 15 L20 3" fill="none" stroke="#A2FF00" stroke-width="5" stroke-linejoin="round"/></svg>Course Admin is Web based meaning you can access your course information from anywhere at any time.</li>
    <li><svg width="22" height="18" viewBox="0 0 22 18" aria-hidden="true"><path d="M2 9 L8 15 L20 3" fill="none" stroke="#A2FF00" stroke-width="5" stroke-linejoin="round"/></svg>System is very intuitive and easy to use.</li>
    <li><svg width="22" height="18" viewBox="0 0 22 18" aria-hidden="true"><path d="M2 9 L8 15 L20 3" fill="none" stroke="#A2FF00" stroke-width="5" stroke-linejoin="round"/></svg>Lighten your workload</li>
    <li><svg width="22" height="18" viewBox="0 0 22 18" aria-hidden="true"><path d="M2 9 L8 15 L20 3" fill="none" stroke="#A2FF00" stroke-width="5" stroke-linejoin="round"/></svg>Upload and manage offline bookings through the admin dashboard</li>
    <li><svg width="22" height="18" viewBox="0 0 22 18" aria-hidden="true"><path d="M2 9 L8 15 L20 3" fill="none" stroke="#A2FF00" stroke-width="5" stroke-linejoin="round"/></svg>Keep your attendees organized all the way up to the course date and<br>beyond</li>
  </ul>

  <h2 class="abs contact-title">Contact Us Now for a free no obligation discussion about your requirement and quote.</h2>

  <form class="abs contact-form">
    <div class="field"><label>Name:</label><span></span></div>
    <div class="field"><label>Company:</label><span></span></div>
    <div class="field"><label>Email:</label><span></span></div>
    <div class="field"><label>Telephone:</label><span></span></div>
    <button class="submit" type="button">SUBMIT</button>
  </form>

  <p class="abs footer">| ©2010 Brightloom Works, All Rights Reserved | Disclaimer |</p>
</div>
</body>
</html>
```